Business Card design for construction company

I would like a business card design for a construction company - Harlow Constructions. I have attached the ai logo file for use. I would like the card to be very smart and clean and incorporate only white and the two colours in the logo. I would like the card to have two sides. One side can just have the logo, the other with the relevant information.

Target Market(s)

Building and Construction Clients

Industry/Entity Type

Business

Contact Information for Business Card

Name: Tom Pardoe
Company: Harlow Constructions Pty Limited
Address: 14 Mallee Crescent Carrow Vale 2093
Phone: 0427 531 068
Email: tomp@harlowbuild-example.com.au

Font styles to use
Serif
Sans Serif

Requirements
Must have
• Details noted above
• Logo as provided
• Colours as in logo
• Square edges
• A font that compliments the logo
Should not have
• Any colour other than white and those in logo
• Rounded edges

```html
<!DOCTYPE html>
<html lang="en">
<head>
<meta charset="utf-8">
<title>Harlow Constructions – Business Card Front</title>
<link rel="stylesheet" href="https://fonts.googleapis.com/css2?family=Michroma&display=swap">
<style>
  :root {
    --card-grey: #a7a8ac;
    --ink-grey: #58595b;
    --accent-blue: #00aeef;
    --frame-white: #ffffff;
    --edge-black: #111111;
  }
  html, body {
    margin: 0;
    padding: 0;
    width: 1200px;
    height: 701px;
    overflow: hidden;
    background: var(--card-grey);
  }
  .card {
    position: relative;
    width: 1200px;
    height: 701px;
    background: var(--card-grey);
  }
  .card-frames {
    position: absolute;
    inset: 0;
  }
  .brand {
    position: absolute;
    left: 0;
    right: 0;
    top: 355px;
    transform: translateY(-50%);
    display: flex;
    align-items: center;
    justify-content: center;
    gap: 26px;
  }
  .brand-mark {
    width: 22px;
    height: 22px;
    background: var(--accent-blue);
  }
  .brand-name {
    margin: 0;
    font-family: "Michroma", "Arial", sans-serif;
    font-weight: 400;
    font-size: 40px;
    letter-spacing: 4px;
    color: var(--ink-grey);
    text-transform: uppercase;
    white-space: nowrap;
  }
</style>
</head>
<body>
  <main class="card">
    <svg class="card-frames" width="1200" height="701" viewBox="0 0 1200 701" aria-hidden="true">
      <rect class="card-edge" x="18" y="18" width="1164" height="665" fill="none" stroke="var(--edge-black)" stroke-width="3"/>
      <polygon class="frame-tilted" points="86,44 1138,100 1109,654 58,599" fill="none" stroke="var(--frame-white)" stroke-width="1.6"/>
      <rect class="frame-straight" x="71" y="71" width="1055" height="557" fill="none" stroke="var(--frame-white)" stroke-width="3.5"/>
    </svg>
    <div class="brand">
      <span class="brand-mark"></span>
      <h1 class="brand-name">Harlow Constructions</h1>
    </div>
  </main>
</body>
</html>
```